Acupuncture Medspa needs a business card design

I need a business card design that looks professional, has a spa-like quality and can offer a promo on the back. Initial promo is "First session free". The tagline of NeedleNook is: Refresh, Restore, Rejuvenate.

NeedleNook is a membership-based acupuncture medspa that offers acupuncture, cupping, and herbal therapies. Members choose between the "Refresh" membership which is for stress relief, or "Restore" which is for treating health conditions, and lastly "Rejuvenate" which is for natural facial enhancement.

Industry/Entity Type

Health And Wellness

Contact Information for Business Card

Coral Haskins, MAC, L.Ac.
612-555-0193
www.needlenook-example.com

Font styles to use
Serif
Sans Serif

Colors

Designer to choose colors to be used in the design.

Requirements
Must have
• The project must have NeedleNook logo, promo on the back, and contact information
Nice to have
• I would like to see the colors of the logo used.

```html
<!DOCTYPE html>
<html lang="en">
<head>
<meta charset="utf-8">
<title>NeedleNook Business Card</title>
<link rel="stylesheet" href="https://fonts.googleapis.com/css2?family=Lato:wght@400;700&display=swap">
<style>
  :root {
    --bg: #e4e4e4;
    --brown: #2e1a0e;
    --teal: #17868a;
    --paper: #fbf7f6;
    --ink: #222222;
    --rule: #b9b9b9;
    --mist: #dde9e8;
    --brown-faint: #3a2416;
    --white: #ffffff;
  }
  * { box-sizing: border-box; margin: 0; padding: 0; }
  html, body { width: 1200px; height: 782px; overflow: hidden; }
  body {
    background: var(--bg);
    font-family: "Lato", sans-serif;
    display: flex;
    align-items: center;
    justify-content: center;
    gap: 44px;
  }
  .card {
    position: relative;
    width: 540px;
    height: 309px;
    overflow: hidden;
    box-shadow: 0 6px 18px rgba(0,0,0,0.18);
  }
  /* Front: promo side */
  .card--promo { background: var(--brown); }
  .promo-brand {
    position: absolute;
    top: 112px; left: 0; right: 0;
    display: flex; align-items: center; justify-content: center; gap: 12px;
    color: var(--teal);
    font-weight: 700;
    font-size: 44px;
    letter-spacing: 1px;
  }
  .brand-dot {
    width: 30px; height: 30px;
    border: 3px solid var(--teal);
    border-radius: 50%;
  }
  .promo-offer {
    position: absolute;
    top: 214px; left: 0; right: 0;
    text-align: center;
    color: var(--white);
    font-weight: 700;
    font-size: 14px;
    letter-spacing: 0.5px;
  }
  .faint-ring {
    position: absolute;
    border-radius: 50%;
  }
  .card--promo .faint-ring {
    width: 230px; height: 230px;
    right: -30px; bottom: -70px;
    border: 6px solid var(--brown-faint);
  }
  /* Back: contact side */
  .card--contact { background: var(--paper); }
  .contact-brand {
    position: absolute;
    left: 58px; top: 50%;
    transform: translate(-50%, -50%) rotate(-90deg);
    display: flex; align-items: center; gap: 8px;
    color: var(--teal);
    font-weight: 700;
    font-size: 30px;
    letter-spacing: 1px;
    white-space: nowrap;
  }
  .contact-brand .brand-dot { width: 22px; height: 22px; border-width: 2px; }
  .divider {
    position: absolute;
    left: 112px; top: 28px; bottom: 28px;
    width: 1px;
    background: var(--rule);
  }
  .card--contact .faint-ring {
    width: 190px; height: 190px;
    right: -20px; bottom: -60px;
    border: 6px solid var(--mist);
  }
  .contact-body {
    position: absolute;
    left: 150px; top: 78px;
  }
  .person-name {
    color: var(--teal);
    font-weight: 700;
    font-size: 17px;
    letter-spacing: 0.4px;
    margin-bottom: 14px;
  }
  .contact-list { list-style: none; }
  .contact-list li {
    display: flex; align-items: center; gap: 8px;
    color: var(--ink);
    font-size: 14px;
    line-height: 20px;
  }
  .contact-list svg { width: 11px; height: 11px; fill: var(--teal); flex: none; }
  .tagline {
    margin-top: 12px;
    color: #444;
    font-size: 13px;
    letter-spacing: 0.4px;
  }
</style>
</head>
<body>
  <section class="card card--promo">
    <div class="faint-ring" aria-hidden="true"></div>
    <div class="promo-brand"><span>NeedleNook</span><span class="brand-dot" aria-hidden="true"></span></div>
    <p class="promo-offer">FIRST SESSION FREE</p>
  </section>

  <section class="card card--contact">
    <div class="faint-ring" aria-hidden="true"></div>
    <div class="contact-brand"><span>NeedleNook</span><span class="brand-dot" aria-hidden="true"></span></div>
    <div class="divider" aria-hidden="true"></div>
    <div class="contact-body">
      <h1 class="person-name">CORAL HASKINS, MAC, L.AC.</h1>
      <ul class="contact-list">
        <li>
          <svg viewBox="0 0 12 12" aria-hidden="true"><path d="M2.5 1h2l1 3-1.3 1a6.5 6.5 0 0 0 2.8 2.8l1-1.3 3 1v2c0 .8-.7 1.5-1.5 1.5A10 10 0 0 1 1 2.5C1 1.7 1.7 1 2.5 1z"/></svg>
          612-555-0193
        </li>
        <li>
          <svg viewBox="0 0 12 12" aria-hidden="true"><path d="M0 2h12v8H0z M0 2l6 4.5L12 2" fill="none" stroke="#17868a" stroke-width="1.4"/></svg>
          coral@needlenook-example.com
        </li>
        <li>
          <svg viewBox="0 0 12 12" aria-hidden="true"><circle cx="6" cy="6" r="5.5"/></svg>
          www.needlenook-example.com
        </li>
      </ul>
      <p class="tagline">REFRESH | RESTORE | REJUVENATE</p>
    </div>
  </section>
</body>
</html>
```